Alterations to existing business card

Here is my current logo and I want the "cafe and bar" taken off with just the words Lumo and our slogan "SAVOUR EVERY SIP" on the card, Plus the logo.
Our Current Business Card is currently 5.5cm by 5.5cm and would like it to remain like this thanks.
The loyalty card can be 10 squares with the logo specifying the 10th coffee free. I would like the cheapest option please.
Also on our business card would like the Facebook logo and instagram Logo with TEAHOUSELUMO27 as link to our photos on instagram.

Keep Colour schemes the same please.

On the business cards

Dale Hartwig Director
0427913608
dale27lumo@examplemail.com

Rosa Delacourt Principal
0428150973
roslumo@examplemail.com

Thanks Dale

```html
<!DOCTYPE html>
<html lang="en">
<head>
<meta charset="utf-8">
<title>Lumo business and loyalty cards</title>
<link rel="stylesheet" href="https://fonts.googleapis.com/css2?family=Saira:wght@300;400;700&family=Questrial&display=swap">
<style>
  :root {
    --stage: #c9a77c;
    --card: #000000;
    --gold: #f2c447;
    --gold-deep: #d3961c;
    --white: #ffffff;
    --faint: #262626;
    --stamp-red: #d62a2a;
    --cup-line: #555555;
    --label: #ffffff;
  }
  * { margin: 0; padding: 0; box-sizing: border-box; }
  html, body { width: 1200px; height: 1000px; overflow: hidden; }
  body { background: var(--stage); position: relative; font-family: "Saira", sans-serif; color: var(--white); }

  .sheet-label { position: absolute; font-family: "Questrial", sans-serif; font-size: 58px; line-height: 1; color: var(--label); }
  .column-label { top: 14px; width: 352px; text-align: center; }
  .row-label-front { left: 40px; top: 458px; }
  .row-label-back { left: 40px; top: 922px; }

  .card { position: absolute; width: 352px; height: 352px; background: var(--card); box-shadow: 0 6px 18px rgba(0,0,0,.45); overflow: hidden; }
  .col-1 { left: 52px; } .col-2 { left: 438px; } .col-3 { left: 825px; }
  .row-front { top: 98px; } .row-back { top: 556px; }

  .brand { position: absolute; display: flex; align-items: center; }
  .brand-mark { border-radius: 50%; border: 3px solid var(--gold); flex: none; }
  .brand-text { display: flex; flex-direction: column; }
  .brand-name { font-weight: 300; color: var(--white); letter-spacing: .02em; line-height: 1; }
  .brand-slogan { font-weight: 400; color: var(--gold); letter-spacing: .08em; line-height: 1; }

  .brand-small { left: 78px; top: 24px; gap: 8px; }
  .brand-small .brand-mark { width: 54px; height: 54px; }
  .brand-small .brand-name { font-size: 34px; }
  .brand-small .brand-slogan { font-size: 8px; margin-top: 2px; padding-left: 2px; }

  .brand-large { left: 26px; top: 110px; gap: 14px; }
  .brand-large .brand-mark { width: 104px; height: 104px; border-width: 4px; }
  .brand-large .brand-name { font-size: 60px; }
  .brand-large .brand-slogan { font-size: 15px; margin-top: 6px; padding-left: 2px; }

  .ghost-ring { position: absolute; left: 58px; top: 100px; width: 240px; height: 240px; border-radius: 50%; border: 6px solid var(--faint); }

  .person-name { position: absolute; left: 21px; top: 118px; font-size: 21px; font-weight: 400; line-height: 1; }
  .rule { position: absolute; left: 20px; top: 145px; width: 311px; height: 3px; background: linear-gradient(90deg, var(--gold-deep), var(--gold)); }
  .person-role { position: absolute; right: 21px; top: 150px; font-size: 17px; line-height: 1.2; }

  .contact-list { position: absolute; left: 26px; top: 200px; list-style: none; }
  .contact-list li { display: flex; align-items: center; height: 31px; font-size: 16px; letter-spacing: .01em; white-space: nowrap; }
  .contact-icon { width: 26px; height: 24px; margin-right: 8px; flex: none; }
  .social-square { width: 24px; height: 24px; border-radius: 4px; background: linear-gradient(180deg, var(--gold), var(--gold-deep)); margin-right: 10px; flex: none; }

  .stamp-grid { position: absolute; left: 21px; top: 115px; display: grid; grid-template-columns: repeat(5, 57px); gap: 8px 5px; }
  .stamp { width: 57px; height: 57px; border-radius: 50%; background: var(--white); border: 3px solid var(--gold); position: relative; display: flex; align-items: center; justify-content: center; }
  .stamp svg { width: 26px; height: 34px; }
  .stamp-free { position: absolute; font-weight: 700; font-size: 14px; color: var(--stamp-red); transform: rotate(-18deg); letter-spacing: .02em; top: 19px; }

  .loyalty-social { position: absolute; left: 28px; top: 263px; list-style: none; }
  .loyalty-social li { display: flex; align-items: center; height: 33px; font-size: 16px; white-space: nowrap; }
  .loyalty-social li:first-child { padding-left: 76px; }
</style>
</head>
<body>
  <div class="sheet-label column-label" style="left:52px">card 1</div>
  <div class="sheet-label column-label" style="left:438px">card 2</div>
  <div class="sheet-label column-label" style="left:825px">card 3</div>
  <div class="sheet-label row-label-front">front</div>
  <div class="sheet-label row-label-back">back</div>

  <!-- Business card: Director -->
  <section class="card col-1 row-front">
    <div class="ghost-ring"></div>
    <div class="brand brand-small"><span class="brand-mark"></span><div class="brand-text"><span class="brand-name">LUMO</span><span class="brand-slogan">SAVOUR EVERY SIP</span></div></div>
    <h2 class="person-name">Dale Hartwig</h2>
    <div class="rule"></div>
    <p class="person-role">Director</p>
    <ul class="contact-list">
      <li><svg class="contact-icon" viewBox="0 0 26 24"><rect x="7" y="1" width="12" height="22" rx="2" fill="none" stroke="var(--gold)" stroke-width="2.5"/><rect x="10" y="5" width="6" height="11" fill="var(--gold)"/></svg>0427913608</li>
      <li><svg class="contact-icon" viewBox="0 0 26 24"><rect x="1" y="4" width="24" height="16" fill="var(--gold)"/><path d="M1 4 L13 14 L25 4" fill="none" stroke="#000" stroke-width="2"/></svg>dale27lumo@examplemail.com</li>
      <li><span class="social-square"></span>@teahouselumo27</li>
      <li><span class="social-square"></span>/Lumo-Tea-418305772619/</li>
    </ul>
  </section>

  <!-- Business card: Principal -->
  <section class="card col-2 row-front">
    <div class="ghost-ring"></div>
    <div class="brand brand-small"><span class="brand-mark"></span><div class="brand-text"><span class="brand-name">LUMO</span><span class="brand-slogan">SAVOUR EVERY SIP</span></div></div>
    <h2 class="person-name">Rosa Delacourt</h2>
    <div class="rule"></div>
    <p class="person-role">Principal</p>
    <ul class="contact-list">
      <li><svg class="contact-icon" viewBox="0 0 26 24"><rect x="7" y="1" width="12" height="22" rx="2" fill="none" stroke="var(--gold)" stroke-width="2.5"/><rect x="10" y="5" width="6" height="11" fill="var(--gold)"/></svg>0428150973</li>
      <li><svg class="contact-icon" viewBox="0 0 26 24"><rect x="1" y="4" width="24" height="16" fill="var(--gold)"/><path d="M1 4 L13 14 L25 4" fill="none" stroke="#000" stroke-width="2"/></svg>roslumo@examplemail.com</li>
      <li><span class="social-square"></span>@teahouselumo27</li>
      <li><span class="social-square"></span>/Lumo-Tea-418305772619/</li>
    </ul>
  </section>

  <!-- Loyalty card -->
  <section class="card col-3 row-front">
    <div class="brand brand-small"><span class="brand-mark"></span><div class="brand-text"><span class="brand-name">LUMO</span><span class="brand-slogan">SAVOUR EVERY SIP</span></div></div>
    <div class="stamp-grid">
      <div class="stamp"><svg viewBox="0 0 26 34"><path d="M2 6 H24 L21 32 H5 Z M1 2 H25 V6 H1 Z" fill="none" stroke="var(--cup-line)" stroke-width="1.5"/></svg></div>
      <div class="stamp"><svg viewBox="0 0 26 34"><path d="M2 6 H24 L21 32 H5 Z M1 2 H25 V6 H1 Z" fill="none" stroke="var(--cup-line)" stroke-width="1.5"/></svg></div>
      <div class="stamp"><svg viewBox="0 0 26 34"><path d="M2 6 H24 L21 32 H5 Z M1 2 H25 V6 H1 Z" fill="none" stroke="var(--cup-line)" stroke-width="1.5"/></svg></div>
      <div class="stamp"><svg viewBox="0 0 26 34"><path d="M2 6 H24 L21 32 H5 Z M1 2 H25 V6 H1 Z" fill="none" stroke="var(--cup-line)" stroke-width="1.5"/></svg></div>
      <div class="stamp"><svg viewBox="0 0 26 34"><path d="M2 6 H24 L21 32 H5 Z M1 2 H25 V6 H1 Z" fill="none" stroke="var(--cup-line)" stroke-width="1.5"/></svg></div>
      <div class="stamp"><svg viewBox="0 0 26 34"><path d="M2 6 H24 L21 32 H5 Z M1 2 H25 V6 H1 Z" fill="none" stroke="var(--cup-line)" stroke-width="1.5"/></svg></div>
      <div class="stamp"><svg viewBox="0 0 26 34"><path d="M2 6 H24 L21 32 H5 Z M1 2 H25 V6 H1 Z" fill="none" stroke="var(--cup-line)" stroke-width="1.5"/></svg></div>
      <div class="stamp"><svg viewBox="0 0 26 34"><path d="M2 6 H24 L21 32 H5 Z M1 2 H25 V6 H1 Z" fill="none" stroke="var(--cup-line)" stroke-width="1.5"/></svg></div>
      <div class="stamp"><svg viewBox="0 0 26 34"><path d="M2 6 H24 L21 32 H5 Z M1 2 H25 V6 H1 Z" fill="none" stroke="var(--cup-line)" stroke-width="1.5"/></svg></div>
      <div class="stamp"><svg viewBox="0 0 26 34"><path d="M2 6 H24 L21 32 H5 Z M1 2 H25 V6 H1 Z" fill="none" stroke="var(--cup-line)" stroke-width="1.5"/></svg><span class="stamp-free">FREE</span></div>
    </div>
    <ul class="loyalty-social">
      <li><span class="social-square"></span>@teahouselumo27</li>
      <li><span class="social-square"></span>/Lumo-Tea-418305772619/</li>
    </ul>
  </section>

  <!-- Card backs -->
  <section class="card col-1 row-back"><div class="brand brand-large"><span class="brand-mark"></span><div class="brand-text"><span class="brand-name">LUMO</span><span class="brand-slogan">SAVOUR EVERY SIP</span></div></div></section>
  <section class="card col-2 row-back"><div class="brand brand-large"><span class="brand-mark"></span><div class="brand-text"><span class="brand-name">LUMO</span><span class="brand-slogan">SAVOUR EVERY SIP</span></div></div></section>
  <section class="card col-3 row-back"><div class="brand brand-large"><span class="brand-mark"></span><div class="brand-text"><span class="brand-name">LUMO</span><span class="brand-slogan">SAVOUR EVERY SIP</span></div></div></section>
</body>
</html>
```